web Design for Architecture and Interior Design Firm

This is a complete redesign of an architecture and interior design firm.( http://www.kelbrixa.com )
We have established a new look-n-feel for them and need to apply it to the new site/new architecture. Wireframes attached with logo and PDF of new brochure.
This will require a quck turn-around. The client is expecting a very modern design with web 2.0 in mind.
Again very quick turn-around! If you cannot commit to a Friday deliverable, do not bid! Must be completed by no later than Friday!

```html
<!DOCTYPE html>
<html lang="en">
<head>
<meta charset="utf-8">
<title>Kelbrixa Design Studios – Website Pages</title>
<link href="https://fonts.googleapis.com/css2?family=Arimo:wght@400;700&display=swap" rel="stylesheet">
<style>
:root{
  --ink:#2a2a2a;
  --text:#555;
  --muted:#888;
  --rule:#d6d6d6;
  --red:#c41230;
  --band:#0d0d0d;
  --backdrop:#746857;
  --paper:#ffffff;
  --overlay:rgba(70,70,70,.82);
}
*{margin:0;padding:0;box-sizing:border-box}
html,body{width:1200px;height:2720px;overflow:hidden}
body{position:relative;background:var(--backdrop);font-family:"Arimo",Arial,sans-serif;color:var(--text)}
.backdrop{position:absolute;inset:0;background:linear-gradient(135deg,#7d705f 0%,#6b5f50 50%,#7a6d5c 100%)}
.band{position:absolute;left:0;width:1200px;height:60px;background:var(--band);color:#fff;font-weight:700;font-size:15px;letter-spacing:.5px;padding-left:187px;display:flex;align-items:center}
.page{position:absolute;left:157px;width:885px;background:var(--paper);box-shadow:0 0 12px rgba(0,0,0,.35)}
.brand{position:absolute;left:60px;font-size:34px;font-weight:700;letter-spacing:1px;color:var(--ink);display:flex;align-items:center;gap:10px}
.brand-mark{width:14px;height:14px;background:var(--red)}
.nav{position:absolute;right:60px;display:flex;font-size:12px;color:var(--ink);text-transform:uppercase}
.nav span{padding:0 9px;border-left:1px solid #bbb;line-height:12px}
.nav span:first-child{border-left:0}
.nav .current{color:var(--red)}
.photo{position:absolute;left:30px;width:825px}
.redbar{position:absolute;left:30px;width:825px;height:8px;background:var(--red)}
.caption-box{position:absolute;right:0;bottom:36px;width:278px;height:85px;background:var(--overlay);color:#fff;font-size:23px;display:flex;align-items:center;padding-left:26px}
.arrow-btn{position:absolute;right:16px;top:50%;margin-top:-22px;width:44px;height:44px;border-radius:50%;background:rgba(255,255,255,.35)}
.footer-rule{position:absolute;left:30px;width:825px;height:1px;background:var(--rule)}
.footer{position:absolute;left:30px;width:825px;display:flex;justify-content:space-between;align-items:center;font-size:11px;color:var(--muted)}
.follow{display:flex;align-items:center;gap:6px}
.follow i{display:block;width:14px;height:14px;background:#444}
h1.lead{position:absolute;left:30px;width:500px;font-size:22px;line-height:26px;color:var(--ink);font-weight:700}
p.body{font-size:12px;line-height:17px;color:var(--text)}
.section-title{position:absolute;font-size:30px;color:var(--red);text-transform:uppercase;font-weight:400}
.news{position:absolute;left:565px;width:290px}
.news h2{font-size:14px;color:var(--ink);font-weight:400;margin-bottom:10px;border-bottom:1px solid var(--rule);padding-bottom:6px}
.news h3{font-size:11px;color:var(--red);font-weight:700}
.news p{font-size:11px;line-height:14px;color:var(--text);margin-bottom:10px}
.thumb{position:absolute;width:203px}
.thumb .pic{height:106px}
.thumb .label{font-size:12px;line-height:16px;color:var(--ink);margin-top:14px;padding-bottom:10px;border-bottom:1px solid var(--rule)}
.sidebar{position:absolute;left:634px;width:221px}
.sidebar ul{list-style:none;margin-top:16px}
.sidebar li{font-size:12px;line-height:17px;color:var(--ink);padding:8px 0 8px 16px;border-bottom:1px solid var(--rule);position:relative}
.sidebar li::before{content:"›";position:absolute;left:2px;color:var(--muted)}
.sidebar li.current{color:var(--red)}
</style>
</head>
<body>
<div class="backdrop" role="img" aria-label="Faint architectural drawings over a warm taupe background"></div>

<!-- Index -->
<div class="band" style="top:0">INDEX PAGE</div>
<section class="page" style="top:54px;height:798px">
  <div class="brand" style="top:40px"><span class="brand-mark"></span>KELBRIXA</div>
  <nav class="nav" style="top:84px"><span class="current">Home</span><span>About Us</span><span>Services</span><span>Portfolio</span><span>Career</span><span>Contact Us</span></nav>
  <div class="photo" style="top:121px;height:429px;background:linear-gradient(180deg,#4a4f5c 0%,#8a7f73 55%,#d9d3cc 100%)" role="img" aria-label="Meeting room with orange chairs and a wall of coloured circular panels">
    <div class="caption-box">Northwind Media Office</div>
  </div>
  <div class="redbar" style="top:550px"></div>
  <h1 class="lead" style="top:580px">Kelbrixa Design Studios Makes the Process Predictable</h1>
  <p class="body" style="position:absolute;left:30px;top:648px;width:500px">When something as important as the very space in which your business lives and works is about to be disrupted, you should be confident you've chosen the right space and the best team to ensure a successful project. Rely on Kelbrixa Design Studios to meet your needs and to make the process predictable. You can be assured that your project goals and objectives will be achieved.</p>
  <div class="news" style="top:580px">
    <h2>NEWS</h2>
    <h3>News Tier 1</h3>
    <p>Lorem ipsum dolor sit amet, consectetur adipiscing elit. Mauris vitae dui nunc. Sed quis lorem. more</p>
    <h3>New Office Location</h3>
    <p>Lorem ipsum dolor sit amet, consectetur adipiscing elit. Mauris vitae dui nunc. Sed quis lorem. more</p>
  </div>
  <div class="footer-rule" style="top:737px"></div>
  <div class="footer" style="top:752px"><span>© 2011 Kelbrixa Design Studios</span><span class="follow">Follow us <i></i><i></i></span></div>
</section>

<!-- Portfolio -->
<div class="band" style="top:906px">PORTFOLIO PAGE</div>
<section class="page" style="top:966px;height:740px">
  <div class="brand" style="top:36px"><span class="brand-mark"></span>KELBRIXA</div>
  <nav class="nav" style="top:78px"><span>Home</span><span>About Us</span><span>Services</span><span class="current">Portfolio</span><span>Career</span><span>Contact Us</span></nav>
  <h2 class="section-title" style="left:30px;top:113px">Portfolio</h2>
  <p class="body" style="position:absolute;left:30px;top:157px;width:155px">Lorem Ipsum is simply dummy text of the printing and typesetting industry. Lorem Ipsum has been the industry's standard dummy text ever since the 1500s, when an unknown printer took a galley of type and scrambled it to make a type specimen book. It has survived not only five centuries, but also the leap into electronic typesetting, remaining essentially unchanged.</p>
  <div class="thumb" style="left:217px;top:121px"><div class="pic" style="background:linear-gradient(180deg,#3c4a66,#8a7a68)" role="img" aria-label="Conference room interior"></div><div class="label">Corvane Systems, Rosslyn and Reston, VA</div></div>
  <div class="thumb" style="left:432px;top:121px"><div class="pic" style="background:linear-gradient(180deg,#cfd2d4,#8f9aa3)" role="img" aria-label="Bright office workspace"></div><div class="label">Halvers Ward, Arlington, VA</div></div>
  <div class="thumb" style="left:649px;top:121px"><div class="pic" style="background:linear-gradient(180deg,#b9c6d2,#a0583f)" role="img" aria-label="Brick office building exterior"></div><div class="label">Kelbrixa and Dunmore Partners Offices</div></div>
  <div class="thumb" style="left:217px;top:302px"><div class="pic" style="height:112px;background:linear-gradient(180deg,#2f5a8c,#c07a3a)" role="img" aria-label="Lobby interior with blue and wood tones"></div><div class="label">Corvane Systems, Falls Church, VA</div></div>
  <div class="thumb" style="left:432px;top:302px"><div class="pic" style="height:112px;background:linear-gradient(180deg,#a11f2a,#3a3d44)" role="img" aria-label="Broadcast studio with red accents"></div><div class="label">Northwind Broadcasting Group (NBG), Washington, D.C.</div></div>
  <div class="footer-rule" style="top:665px"></div>
  <div class="footer" style="top:684px"><span>© 2011 Kelbrixa Design Studios</span><span class="follow">Follow us <i></i><i></i></span></div>
</section>

<!-- Detail -->
<div class="band" style="top:1745px">DETAIL PORTFOLIO PAGE</div>
<section class="page" style="top:1806px;height:914px">
  <div class="brand" style="top:30px"><span class="brand-mark"></span>KELBRIXA</div>
  <nav class="nav" style="top:72px"><span>Home</span><span>About Us</span><span>Services</span><span class="current">Portfolio</span><span>Career</span><span>Contact Us</span></nav>
  <div class="photo" style="top:112px;height:422px;background:linear-gradient(90deg,#6e6a66 0%,#d8d4ce 40%,#eceae6 65%,#2f4f86 100%)" role="img" aria-label="Home office with white bookshelves, desk and a window view at dusk">
    <div class="arrow-btn"><svg width="44" height="44" viewBox="0 0 44 44"><path d="M19 14l8 8-8 8" fill="none" stroke="#fff" stroke-width="3"/></svg></div>
  </div>
  <div class="redbar" style="top:534px"></div>
  <h1 class="lead" style="top:576px;font-size:25px;font-weight:400">Halvers Ward, Arlington, VA</h1>
  <p class="body" style="position:absolute;left:30px;top:614px;width:580px">When something as important as the very space in which your business lives and works is about to be disrupted, you should be confident you've chosen the right space and the best team to ensure a successful project. Rely on Kelbrixa Design Studios to meet your needs and to make the process predictable. You can be assured that your project goals and objectives will be achieved.</p>
  <p class="body" style="position:absolute;left:30px;top:702px;width:580px">Lorem Ipsum is simply dummy text of the printing and typesetting industry. Lorem Ipsum has been the industry's standard dummy text ever since the 1500s, when an unknown printer took a galley of type and scrambled it to make a type specimen book. It has survived not only five centuries, but also the leap into electronic typesetting, remaining essentially unchanged. It was popularised in the 1960s with the release of sheets containing Lorem Ipsum passages, and more recently with desktop publishing software including versions of Lorem Ipsum.</p>
  <div class="sidebar" style="top:576px">
    <h2 class="section-title" style="position:static;font-size:26px">Portfolio</h2>
    <ul>
      <li>Corvane Systems, Rosslyn and Reston, VA</li>
      <li class="current">Halvers Ward, Arlington, VA</li>
      <li>Kelbrixa and Dunmore Partners Offices</li>
      <li>Corvane Systems, Falls Church, VA</li>
      <li>Northwind Broadcasting Group (NBG), Washington, D.C.</li>
    </ul>
  </div>
  <div class="footer-rule" style="top:852px"></div>
  <div class="footer" style="top:872px"><span>© 2011 Kelbrixa Design Studios</span><span class="follow">Follow us <i></i><i></i></span></div>
</section>
</body>
</html>
```